Women's Jewellery startup needs a captivating, beautifully designed and intuitive online store

[12/24 update]

Added 2 additional documents:

Feedback on designs received so far: designer feedback.docx
Product images from catalogue: products images.docx

Please read the feedback provided on designs provided so far to guide you further on your submission. The product images can be used to create promotional banners for the site.

@@@Added a document (VELISSE JEWELLERY_checklist.docx) which can be used by designers as a checklist when submitting their designs to ensure all aspects of the requirements have been covered @@@

+++IMPORTANT BUT NOT SPECIFIED IN THE REQUIREMENTS DOCUMENT - DESIGN SHOULD INCLUDE SUPPORT FOR MOBILE FRIENDLY SITE TOO+++

***Previous experience designing Jewellery online stores preferred (not essential)***

The name of the online Jewellery store is "Velisse Jewellery" and the business is based in Hong Kong. It will be run by 2 stay at home mothers. We need a Shopify themed store designed that will achieve the following objectives in order of priority:

• Conversion: The primary objective of the design/content is to prompt the customer to make a purchase. While this may sound obvious, it is mentioned so as not to distract the design process by focusing on other objectives (which are also important). The site also needs to be optimized so as to rank high in search engine searches for relevant keywords (SEO)
• Navigation: An intuitive interface which takes away a lot of the thinking from the customer by making it obvious what they need to do when they visit the store
• Engagement: Encourages the customer to spend time on the website and share content with their social network

Where applicable, the design of the store should reflect as closely as possible the mission statements and words outlined below:

• Jewellery you’ll fall in love with
• We want every client to leave the store with a smile
• We want to be able to provide the best service we can in every situation no matter what
• We aim to increase our business by word of mouth; therefore we tell people things about our store that makes it interesting for them to share
• We love every customer, no matter how difficult things get
• We, as a team, are so well informed about our products and brands that we always have the best information for our customers
• We celebrate women here!
• We celebrate life in here!
• We celebrate beauty here!
• We celebrate families here, as jewellery often stays within families.
• We will always try to make an extra step
• We will always try to exceed the expectation of our customers
• We will go as far as we possibly can to attract a customer back to our store and connect with us
• Every client that leaves our store knows more about jewellery because we passionately told him about it
• Romantic, classic, love, warm, cool, stylish

A draft functional specification is attached with this brief. We would like the design to reflect as closely as possible the functional requirements outlined in the document. Open to suggestions to improve upon the functional requirements.

Target Market(s)

Women aged 18-55

Industry/Entity Type

Jewelry Store

Coding

Coded - Design and coding required

Number of Pages Required

5+ page

Font styles to use
Other font styles liked:
• Myriad Pro as per Logo but open to any font that complements this one

Requirements
Must have
• 1. A look that encourages the user to make a purchase
• 2. An intuitive, easy to navigate and engaging interface
• 3. Primary colour scheme as defined in the functional specification attached
• 4. Simplistic look, not too cluttered
Nice to have
• 1. Closely matching the functional requirements of the site as outlined in the requirements specification but open to any better ideas

```html
<!DOCTYPE html>
<html lang="en">
<head>
<meta charset="utf-8">
<title>Velisse Jewellery</title>
<link href="https://fonts.googleapis.com/css2?family=Montserrat:wght@400;500;600&family=Open+Sans:wght@400;600&family=Arimo:wght@400;700&display=swap" rel="stylesheet">
<style>
:root{
  --gold:#d4a21c;
  --gold-soft:#c9a24a;
  --ink:#111;
  --panel:#1c1c1c;
  --band:#050505;
  --muted:#8c8c8c;
  --frame:#e6e6e6;
  --white:#fff;
}
*{box-sizing:border-box;margin:0;padding:0}
html,body{width:946px;height:1200px;overflow:hidden;background:var(--frame)}
body{font-family:"Open Sans",sans-serif;position:relative}
.page{position:absolute;left:11px;top:11px;width:923px;height:1178px;background:var(--panel);overflow:hidden}
.abs{position:absolute}

/* header */
.site-header{left:0;top:0;width:923px;height:113px;background:var(--white)}
.brand{left:24px;top:30px;display:flex;align-items:center;gap:14px}
.brand-mark{width:44px;height:44px;border-radius:50%;background:var(--gold-soft)}
.brand-name{font-family:"Montserrat",sans-serif;font-weight:400;font-size:30px;letter-spacing:13px;color:var(--gold-soft)}
.utility{right:22px;top:19px;display:flex;align-items:center;gap:18px;font-family:"Montserrat",sans-serif;font-size:10px;letter-spacing:.5px;color:#555}
.utility span{display:flex;align-items:center;gap:6px}
.utility svg{display:block}
.search{width:96px;height:15px;border:1px solid #888;border-radius:8px;font-size:7px;padding-left:5px;line-height:13px;color:#666}
.hotline{right:24px;top:64px;display:flex;align-items:center;gap:8px;font-family:"Open Sans",sans-serif;font-size:20px;color:var(--gold)}

/* nav */
.main-nav{left:0;top:113px;width:923px;height:29px;background:var(--band);display:flex;justify-content:center;align-items:center;gap:14px;font-family:"Montserrat",sans-serif;font-weight:600;font-size:10px;color:#ddd;letter-spacing:.3px}
.main-nav i{font-style:normal;color:#aaa;font-weight:400}

/* hero */
.hero{left:0;top:142px;width:923px;height:389px;background:linear-gradient(100deg,#b9b3ad 0%,#cdb7a8 30%,#d9bfb0 50%,#a89c92 75%,#8d8983 100%)}
.hero-copy{left:562px;top:90px;width:300px;color:var(--white)}
.hero-title{font-family:"Montserrat",sans-serif;font-size:15px;letter-spacing:.5px;font-weight:400}
.hero-title b{color:var(--gold);font-weight:600}
.hero-rule{width:290px;height:1px;background:rgba(255,255,255,.7);margin:10px 0 15px}
.hero-text{font-size:8.6px;line-height:14px}
.btn-more{margin-top:24px;width:128px;height:26px;background:#0c0c0c;border:1px solid #fff;font-family:"Montserrat",sans-serif;font-size:11.5px;line-height:24px;text-align:center;letter-spacing:.5px}

/* collections */
.collections{left:40px;top:582px;display:flex;gap:11px}
.card{width:160px;height:189px;background:#0d0d0d;box-shadow:0 4px 8px rgba(0,0,0,.6);position:relative}
.card-head{height:43px;text-align:center;font-family:"Arimo",sans-serif;font-weight:700;font-size:11.5px;color:var(--white);padding-top:13px}
.card-head::after{content:"";display:block;width:116px;height:1px;background:#777;margin:8px auto 0}
.card-img{height:75px}
.c1{background:linear-gradient(90deg,#f2f2f2,#e9e6ee 55%,#f4f4f4)}
.c2{background:linear-gradient(90deg,#2a2a2a,#9a9a9a 50%,#d9d9d9)}
.c3{background:linear-gradient(180deg,#e4e1dc,#b9b2a8)}
.c4{background:linear-gradient(180deg,#e4a583,#c98a6a)}
.c5{background:linear-gradient(90deg,#555,#c9c9c9 60%,#e6e6e6)}
.card-meta{height:34px;display:flex;align-items:center;padding-left:9px;gap:9px;font-size:9.5px;color:#999;font-family:"Montserrat",sans-serif;background:#111}
.card-meta .price{display:flex;align-items:center;gap:9px;margin-right:12px}
.card-meta .cmp{display:flex;align-items:center;gap:5px;font-size:8.5px}
.card-cta{height:37px;background:linear-gradient(#111,#000);text-align:center;line-height:37px;font-family:"Montserrat",sans-serif;font-size:8.8px;letter-spacing:1px;color:#8a8a8a}

/* newsletter */
.newsletter{left:0;top:839px;width:923px;height:88px;background:var(--band);border-bottom:2px solid var(--gold)}
.nl-title{left:73px;top:35px;font-family:"Arimo",sans-serif;font-size:13px;color:#eee}
.nl-title::after{content:"";display:block;width:116px;height:1px;background:#777;margin:5px auto 0}
.field{top:43px;height:27px;border:2px solid #fff;border-radius:2px;background:linear-gradient(#000,#1a1a1a);color:#fff;font-family:"Montserrat",sans-serif;font-size:11px;line-height:23px;padding-left:11px}
.f-name{left:419px;width:151px}
.f-mail{left:579px;width:151px}
.f-submit{left:739px;width:129px;padding:0;text-align:center;background:linear-gradient(#2a2a2a,#111);border-color:#ccc}

/* footer */
.footer-mark{left:82px;top:975px;font-family:"Montserrat",sans-serif;font-size:16px;letter-spacing:5px;color:#6a6a6a}
.fcol{top:972px}
.fcol h4{font-family:"Arimo",sans-serif;font-size:13px;font-weight:700;color:var(--gold);padding-bottom:7px;border-bottom:1px solid #333;width:92px;margin-bottom:13px}
.fcol h4.light{font-weight:400;width:108px}
.fcol li{list-style:none;font-size:10.5px;line-height:14.5px;color:#999;letter-spacing:.8px}
.col-nav{left:219px}
.col-info{left:351px}
.col-acct{left:502px}
.info-box{left:627px;top:963px;width:216px;height:150px;border:2px solid var(--gold);border-radius:4px;text-align:center;color:var(--gold)}
.info-box .lead{font-family:"Arimo",sans-serif;font-size:12px;margin-top:10px}
.info-box .tel{display:flex;align-items:center;justify-content:center;gap:6px;font-family:"Arimo",sans-serif;font-weight:700;font-size:20px;color:#fff;margin-top:4px}
.info-box .addr{font-size:11.5px;line-height:14px;letter-spacing:.5px;margin-top:14px}
.social{display:flex;justify-content:center;gap:4px;margin-top:13px}
.social i{width:12px;height:12px;border-radius:50%;background:#888}
.legal{left:0;top:1149px;width:923px;height:29px;background:var(--band);text-align:center;font-size:7.5px;font-weight:600;color:#bbb;line-height:29px}
</style>
</head>
<body>
<div class="page">
  <header class="site-header abs">
    <div class="brand abs"><span class="brand-mark"></span><span class="brand-name">VELISSE</span></div>
    <div class="utility abs">
      <span><svg width="9" height="10" viewBox="0 0 9 10"><circle cx="4.5" cy="3" r="2.5" fill="#d4a21c"/><path d="M0 10a4.5 4 0 0 1 9 0z" fill="#d4a21c"/></svg>LOGIN</span>
      <span><svg width="10" height="10" viewBox="0 0 10 10"><circle cx="5" cy="5" r="4.3" fill="none" stroke="#d4a21c"/><path d="M5 3v4M3 5h4" stroke="#d4a21c"/></svg>REGISTER</span>
      <span><svg width="11" height="10" viewBox="0 0 11 10"><path d="M5.5 9 1.3 5A2.4 2.4 0 0 1 5.5 1.8 2.4 2.4 0 0 1 9.7 5z" fill="none" stroke="#d4a21c" stroke-width="1.3"/></svg>WISH LIST</span>
      <span><svg width="11" height="10" viewBox="0 0 11 10"><path d="M0 1h2l1.5 5h6l1-3.5H3" fill="none" stroke="#d4a21c" stroke-width="1.2"/><circle cx="4" cy="8.5" r="1" fill="#d4a21c"/><circle cx="8.5" cy="8.5" r="1" fill="#d4a21c"/></svg>CART</span>
      <span><svg width="10" height="10" viewBox="0 0 10 10"><circle cx="4" cy="4" r="3" fill="none" stroke="#222" stroke-width="1.5"/><path d="M6.2 6.2 9.3 9.3" stroke="#222" stroke-width="1.6"/></svg><span class="search">SEARCH</span></span>
    </div>
    <div class="hotline abs">
      <svg width="24" height="24" viewBox="0 0 24 24"><circle cx="12" cy="12" r="11" fill="none" stroke="#555" stroke-width="1.5"/><path d="M8 6.5c-1.5 1 -1.5 3 .5 6s4.5 5 6 4l1.2-1.2-2.2-2-1.2.8c-1-.5-2.4-2-3-3l.8-1.2-2-2.3z" fill="#555"/></svg>
      800-555-0142
    </div>
  </header>

  <nav class="main-nav abs">
    <span>HOME</span><i>I</i><span>ABOUT US</span><i>I</i><span>COLLECTIONS</span><i>I</i><span>WHY CHOOSE US</span><i>I</i><span>NEWS</span><i>I</i><span>GIFT CERTIFICATES</span><i>I</i><span>CONTACT</span>
  </nav>

  <section class="hero abs" role="img" aria-label="Portrait of a woman wearing an ornate gold drop earring">
    <div class="hero-copy abs">
      <h1 class="hero-title">WELCOME TO <b>VELISSE</b></h1>
      <div class="hero-rule"></div>
      <p class="hero-text">Lorem ipsum dolor sit amet, consectetuer adipiscing elit, sed diam no nummy nibh euismod tincidunt ut laoreet dolore magna aliquam erat volutpat. Ut wisi enim ad minim veniam, quis nostrud exerci tation ullam corper suscipit lobortis nisl ut aliquip ex ea commodo consequat.</p>
      <div class="btn-more">Read More</div>
    </div>
  </section>

  <section class="collections abs">
    <article class="card"><h3 class="card-head">Collection #1</h3><div class="card-img c1" role="img" aria-label="Ring with a purple oval stone"></div>
      <div class="card-meta"><span class="price"><svg width="15" height="15" viewBox="0 0 15 15"><circle cx="7.5" cy="7.5" r="6.5" fill="none" stroke="#999"/><text x="7.5" y="10.5" font-size="8" text-anchor="middle" fill="#999">$</text></svg>19.99</span><span class="cmp"><svg width="13" height="13" viewBox="0 0 13 13"><circle cx="6.5" cy="6.5" r="5.7" fill="none" stroke="#999"/><rect x="4" y="4" width="5" height="5" fill="none" stroke="#999" stroke-width=".8"/></svg>compare</span></div>
      <div class="card-cta">CHOOSE OPTIONS</div></article>
    <article class="card"><h3 class="card-head">Collection #2</h3><div class="card-img c2" role="img" aria-label="Stacked silver rings in black and white"></div>
      <div class="card-meta"><span class="price"><svg width="15" height="15" viewBox="0 0 15 15"><circle cx="7.5" cy="7.5" r="6.5" fill="none" stroke="#999"/><text x="7.5" y="10.5" font-size="8" text-anchor="middle" fill="#999">$</text></svg>19.99</span><span class="cmp"><svg width="13" height="13" viewBox="0 0 13 13"><circle cx="6.5" cy="6.5" r="5.7" fill="none" stroke="#999"/><rect x="4" y="4" width="5" height="5" fill="none" stroke="#999" stroke-width=".8"/></svg>compare</span></div>
      <div class="card-cta">CHOOSE OPTIONS</div></article>
    <article class="card"><h3 class="card-head">Collection #3</h3><div class="card-img c3" role="img" aria-label="Diamond solitaire ring"></div>
      <div class="card-meta"><span class="price"><svg width="15" height="15" viewBox="0 0 15 15"><circle cx="7.5" cy="7.5" r="6.5" fill="none" stroke="#999"/><text x="7.5" y="10.5" font-size="8" text-anchor="middle" fill="#999">$</text></svg>19.99</span><span class="cmp"><svg width="13" height="13" viewBox="0 0 13 13"><circle cx="6.5" cy="6.5" r="5.7" fill="none" stroke="#999"/><rect x="4" y="4" width="5" height="5" fill="none" stroke="#999" stroke-width=".8"/></svg>compare</span></div>
      <div class="card-cta">CHOOSE OPTIONS</div></article>
    <article class="card"><h3 class="card-head">Collection #4</h3><div class="card-img c4" role="img" aria-label="Fine silver open bangle with two stones"></div>
      <div class="card-meta"><span class="price"><svg width="15" height="15" viewBox="0 0 15 15"><circle cx="7.5" cy="7.5" r="6.5" fill="none" stroke="#999"/><text x="7.5" y="10.5" font-size="8" text-anchor="middle" fill="#999">$</text></svg>19.99</span><span class="cmp"><svg width="13" height="13" viewBox="0 0 13 13"><circle cx="6.5" cy="6.5" r="5.7" fill="none" stroke="#999"/><rect x="4" y="4" width="5" height="5" fill="none" stroke="#999" stroke-width=".8"/></svg>compare</span></div>
      <div class="card-cta">CHOOSE OPTIONS</div></article>
    <article class="card"><h3 class="card-head">Collection #5</h3><div class="card-img c5" role="img" aria-label="Ornate silver cocktail ring"></div>
      <div class="card-meta"><span class="price"><svg width="15" height="15" viewBox="0 0 15 15"><circle cx="7.5" cy="7.5" r="6.5" fill="none" stroke="#999"/><text x="7.5" y="10.5" font-size="8" text-anchor="middle" fill="#999">$</text></svg>19.99</span><span class="cmp"><svg width="13" height="13" viewBox="0 0 13 13"><circle cx="6.5" cy="6.5" r="5.7" fill="none" stroke="#999"/><rect x="4" y="4" width="5" height="5" fill="none" stroke="#999" stroke-width=".8"/></svg>compare</span></div>
      <div class="card-cta">CHOOSE OPTIONS</div></article>
  </section>

  <section class="newsletter abs">
    <h2 class="nl-title abs">SUBSCRIBE FOR NEWSLETTER</h2>
    <div class="field f-name abs">Name</div>
    <div class="field f-mail abs">Email</div>
    <div class="field f-submit abs">Submit</div>
  </section>

  <footer>
    <div class="footer-mark abs">VELISSE</div>
    <div class="fcol col-nav abs"><h4>Navigation</h4><ul><li>Home</li><li>About Us</li><li>Collections</li><li>Why Choose Us</li><li>News</li><li>Gift Certificates</li><li>Contact</li></ul></div>
    <div class="fcol col-info abs"><h4 class="light">Information</h4><ul><li>Faqs</li><li>Terms &amp; Conditions</li><li>Shipping &amp; Returns</li></ul></div>
    <div class="fcol col-acct abs"><h4>My Account</h4><ul><li>Account</li><li>My Cart</li><li>Order History</li><li>Wish List</li></ul></div>
    <div class="info-box abs">
      <p class="lead">FOR MORE INFORMATION</p>
      <p class="tel"><svg width="26" height="26" viewBox="0 0 24 24"><circle cx="12" cy="12" r="11" fill="none" stroke="#fff" stroke-width="1.5"/><path d="M8 6.5c-1.5 1 -1.5 3 .5 6s4.5 5 6 4l1.2-1.2-2.2-2-1.2.8c-1-.5-2.4-2-3-3l.8-1.2-2-2.3z" fill="#fff"/></svg>(800) 555-0142</p>
      <p class="addr">18 Lantern Lane, Wan Chai<br>Hong Kong</p>
      <div class="social"><i></i><i></i><i></i><i></i></div>
    </div>
    <div class="legal abs">COPYRIGHT © 2017 VELISSE. ALL RIGHTS RESERVED.</div>
  </footer>
</div>
</body>
</html>
```